Modernise Business Card

Our company has been operating for 10 years. With the start of the new decade we are looking to refresh our business card design. We manufacture a range of industrial product shipping to customers internationally. A copy of our current card, both sides, is attached. We are looking for a mature professional appearance.

```html
<!DOCTYPE html>
<html lang="en">
<head>
<meta charset="utf-8">
<title>Kelvrax Business Card</title>
<link rel="stylesheet" href="https://fonts.googleapis.com/css2?family=Montserrat:wght@700&family=Open+Sans:wght@600&family=Arimo:wght@400&display=swap">
<style>
  :root {
    --bg: #e4e4e6;
    --brown: #54402f;
    --blue: #1aa3d4;
    --white: #ffffff;
    --ink: #2a2a2a;
  }
  * { box-sizing: border-box; margin: 0; padding: 0; }
  html, body { width: 1200px; height: 900px; overflow: hidden; }
  body {
    background: var(--bg);
    font-family: "Arimo", Arial, sans-serif;
    position: relative;
  }
  .card {
    position: absolute;
    top: 300px;
    width: 520px;
    height: 300px;
    border-radius: 22px;
    box-shadow: 0 6px 18px rgba(0,0,0,0.18);
    overflow: hidden;
  }
  .card--back { left: 50px; background: var(--brown); }
  .card--front { left: 630px; background: var(--white); }

  .brand-name {
    font-family: "Montserrat", Arial, sans-serif;
    font-weight: 700;
    color: var(--blue);
    letter-spacing: 1px;
    position: absolute;
  }
  .card--back .brand-name { left: 0; right: 0; top: 96px; text-align: center; font-size: 60px; }
  .tagline {
    position: absolute;
    left: 0; right: 0; bottom: 40px;
    text-align: center;
    font-family: "Open Sans", Arial, sans-serif;
    font-weight: 600;
    font-size: 13px;
    letter-spacing: 0.8px;
    text-transform: uppercase;
    color: var(--white);
  }
  .tagline .dot {
    display: inline-block;
    width: 7px; height: 7px;
    border-radius: 50%;
    background: var(--blue);
    margin: 0 6px;
    vertical-align: 2px;
  }

  .card--front .brand-name { left: 34px; top: 34px; font-size: 48px; }
  .person-name {
    position: absolute;
    left: 34px; top: 142px;
    font-family: "Montserrat", Arial, sans-serif;
    font-weight: 700;
    font-size: 21px;
    color: var(--blue);
  }
  .contact-list {
    position: absolute;
    left: 34px; top: 178px;
    list-style: none;
    font-size: 15.5px;
    color: var(--ink);
    line-height: 23px;
  }
  .contact-list li { display: flex; align-items: center; gap: 8px; }
  .contact-list svg { width: 16px; height: 16px; flex: none; }
  .contact-list .region { color: var(--blue); }
  .address {
    position: absolute;
    right: 30px; top: 146px;
    text-align: right;
    font-size: 15px;
    line-height: 20px;
    color: var(--ink);
  }
</style>
</head>
<body>
  <section class="card card--back">
    <div class="brand-name">Kelvrax</div>
    <p class="tagline">Hydraulic Adapters<span class="dot"></span>Host Fittings<span class="dot"></span>Quick Couplings</p>
  </section>

  <section class="card card--front">
    <div class="brand-name">Kelvrax</div>
    <h1 class="person-name">Alan Brewer</h1>
    <ul class="contact-list">
      <li>
        <svg viewBox="0 0 16 16"><path fill="#1aa3d4" d="M3 2h3l1 4-2 1c1 2 2 3 4 4l1-2 4 1v3c0 1-1 1-2 1C7 14 2 9 2 3c0-1 0-1 1-1z"/></svg>
        <span>+86 139 5520 0847 <span class="region">(China)</span></span>
      </li>
      <li>
        <svg viewBox="0 0 16 16"><path fill="#1aa3d4" d="M3 2h3l1 4-2 1c1 2 2 3 4 4l1-2 4 1v3c0 1-1 1-2 1C7 14 2 9 2 3c0-1 0-1 1-1z"/></svg>
        <span>+61 412 730 915 <span class="region">(Australia)</span></span>
      </li>
      <li>
        <svg viewBox="0 0 16 16"><rect x="1" y="3" width="14" height="10" rx="1.5" fill="#1aa3d4"/><path d="M2 4l6 5 6-5" stroke="#fff" stroke-width="1.3" fill="none"/></svg>
        <span>abrewer@kelvraxfittings.com</span>
      </li>
      <li>
        <svg viewBox="0 0 16 16"><circle cx="8" cy="8" r="7" fill="#1aa3d4"/><path d="M1 8h14M8 1c-3 4-3 10 0 14M8 1c3 4 3 10 0 14" stroke="#fff" stroke-width="1" fill="none"/></svg>
        <span>www.kelvraxfittings.com</span>
      </li>
    </ul>
    <address class="address" style="font-style:normal">
      1208-4, Lin Feng Building<br>
      76 Huaxin Road, Haishu<br>
      District Ningbo 315000 China
    </address>
  </section>
</body>
</html>
```